New Body Mist 250 ml exclusive

We are excited to embark on a new project to design the packaging for body mist:
Amber Drizzle

We are looking for a design that is truly unique and stands out, with a touch of individuality that sets it apart. The design should be eye-catching and visually appealing, drawing attention even from a distance. We want the body mists to have a fun and attractive look that appeals to customers.

To help bring your design to life, we will provide the dimensions of the bottle, which has a capacity of 250ml. The bottle measures 13.3 cm in height and 4.9 cm in diameter (excluding the pump). Additionally, we will also provide the dimensions of the label, which measures 15.1 cm in height and 12.8 cm in width.

We believe that giving you the freedom to put your own unique touch and color choices will help create a truly standout design. We look forward to seeing your creative vision for our body mist.

We shared with you the logo of the body mist and some examples of models that we liked.

Please be informed that the project only includes one design and the remaining three will be completed and paid for through a 1on1 project with the winner of the contest.

Target Market(s)

Supermarket and perfumery stores

Industry/Entity Type

Cosmetics

Font styles to use
Serif

Requirements
Must have
• Uniqueness and attractiveness

```html
<!DOCTYPE html>
<html lang="en">
<head>
<meta charset="utf-8">
<title>Amber Drizzle — Body Mist Label</title>
<link rel="stylesheet" href="https://fonts.googleapis.com/css2?family=Cormorant+SC:wght@600&display=swap">
<style>
  :root {
    --backdrop: #ececec;
    --label-top: #fde7ef;
    --label-bottom: #f6dcf6;
    --floral-rose: #f4b9b4;
    --floral-peach: #e8b98f;
    --floral-blue: #a9bedf;
    --plaque-fill: #f6f6f6;
    --plaque-edge: #b3b3b3;
    --ink: #141414;
  }
  html, body {
    margin: 0;
    width: 1200px;
    height: 1200px;
    overflow: hidden;
    background: var(--backdrop);
  }
  .canvas {
    position: relative;
    width: 1200px;
    height: 1200px;
  }
  .label {
    position: absolute;
    left: 411px;
    top: 57px;
    width: 378px;
    height: 1085px;
    background: linear-gradient(180deg, var(--label-top) 0%, var(--label-bottom) 100%);
    overflow: hidden;
  }
  .floral-artwork {
    position: absolute;
    left: 0;
    top: 0;
    width: 378px;
    height: 1085px;
    display: block;
  }
  .name-plaque {
    position: absolute;
    left: 27px;
    top: 355px;
    width: 328px;
    height: 207px;
  }
  .name-plaque svg {
    position: absolute;
    inset: 0;
  }
  .product-name {
    position: absolute;
    inset: 0;
    display: flex;
    align-items: center;
    justify-content: center;
    margin: 0;
    font-family: "Cormorant SC", serif;
    font-weight: 600;
    font-size: 38px;
    letter-spacing: 0.1em;
    color: var(--ink);
    white-space: nowrap;
  }
</style>
</head>
<body>
<main class="canvas">
  <section class="label">
    <svg class="floral-artwork" viewBox="0 0 378 1085" preserveAspectRatio="none" role="img" aria-label="Watercolour bouquet of blush roses with peach and dusty blue leaves and fine brown twigs">
      <defs>
        <radialGradient id="bouquet-tone" cx="0.78" cy="0.55" r="0.75">
          <stop offset="0" stop-color="#f4b9b4" stop-opacity="0.95"/>
          <stop offset="0.45" stop-color="#e8b98f" stop-opacity="0.7"/>
          <stop offset="0.75" stop-color="#a9bedf" stop-opacity="0.35"/>
          <stop offset="1" stop-color="#a9bedf" stop-opacity="0"/>
        </radialGradient>
      </defs>
      <rect x="0" y="0" width="378" height="1085" fill="url(#bouquet-tone)"/>
    </svg>

    <div class="name-plaque">
      <svg viewBox="0 0 328 207" width="328" height="207" aria-hidden="true">
        <path d="M20,45 H80 C80,15 100,4 130,4 H198 C228,4 248,15 248,45 H308 Q324,45 324,61 V146 Q324,162 308,162 H248 C248,192 228,203 198,203 H130 C100,203 80,192 80,162 H20 Q4,162 4,146 V61 Q4,45 20,45 Z"
              fill="var(--plaque-fill)" stroke="var(--plaque-edge)" stroke-width="4"/>
      </svg>
      <h1 class="product-name">Amber Drizzle</h1>
    </div>
  </section>
</main>
</body>
</html>
```